Brennock Metal recycling, a business card/logo for our industrial family metal recycling company

A new business card design/logo for our long established family metal recycling company.
I have a logo for our property company which was designed a few months ago on pixel forum which I would like to be very close to this design but have a more industrial feel to it and in a darker blue colour, please see attachments.

Target Market(s)

industries that produce metal waste for recycling, construction sites, engineering companies, manufactures, builders, plumbers, electricians, general house holders.

Industry/Entity Type

Recycling

Contact Information for Business Card

owner/director...Gordon brennock
e-mail....info@brennockscrapworks.example.co.uk
web address.....brennockscrapworks.example.co.uk

Font styles to use
Serif
Sans Serif

Colors
0255a3
ffffff

Requirements
Must have
• -dark blue business card on front.
-white on the back, see contact details, e-mail address for metal company.
-to have an industrial feel to it.
-brennock logo as business card attached but (brennock metal recycling)
please remove the little roof/arrow above brennock as this was relevant to property company.
Nice to have
• please see our website brennockscrapworks.example.co.uk with all details
being correct however I would like to refresh the logo to more like the brennock property investment business card logo attached.
Should not have
• should not contain details from property investments card as this design is for the metal recycling company.

```html
<!DOCTYPE html>
<html lang="en">
<head>
<meta charset="utf-8">
<title>Brennock Metal Recycling – Business Card</title>
<link href="https://fonts.googleapis.com/css2?family=Quicksand:wght@300;400&family=Roboto+Condensed:wght@700&family=Roboto:wght@400;500&display=swap" rel="stylesheet">
<style>
  :root {
    --navy: #031f4e;
    --paper: #fbfafa;
    --stage: #b2c1d4;
    --light-ink: #ecebe8;
  }
  * { margin: 0; padding: 0; box-sizing: border-box; }
  html, body { width: 1200px; height: 1200px; overflow: hidden; }
  body { background: var(--stage); position: relative; font-family: "Roboto", Arial, sans-serif; }

  .card { position: absolute; left: 285px; width: 630px; height: 360px; }
  .card--contact {
    top: 150px;
    background: var(--paper);
    border-left: 6px solid var(--navy);
    border-bottom: 6px solid var(--navy);
    color: var(--navy);
  }
  .card--brand { top: 604px; background: var(--navy); color: var(--light-ink); }

  .wordmark { position: absolute; left: 0; right: 0; text-align: center; }
  .wordmark__name {
    display: block;
    font-family: "Quicksand", Arial, sans-serif;
    font-weight: 300;
    line-height: 1;
    letter-spacing: 0.02em;
  }
  .wordmark__tagline {
    display: block;
    font-family: "Quicksand", Arial, sans-serif;
    font-weight: 300;
    text-transform: uppercase;
    line-height: 1;
  }
  .card--contact .wordmark { top: 108px; }
  .card--contact .wordmark__name { font-size: 68px; }
  .card--contact .wordmark__tagline { font-size: 13px; letter-spacing: 1.05em; margin-top: 6px; padding-left: 1em; }
  .card--brand .wordmark { top: 110px; }
  .card--brand .wordmark__name { font-size: 108px; }
  .card--brand .wordmark__tagline { font-size: 20px; letter-spacing: 1.05em; margin-top: 10px; padding-left: 1em; }

  .person { position: absolute; right: 366px; top: 227px; text-align: right; }
  .person__name { font-family: "Roboto Condensed", Arial, sans-serif; font-weight: 700; font-size: 28px; line-height: 1; }
  .person__role { font-size: 16px; font-weight: 500; margin-top: 5px; }

  .divider { position: absolute; left: 264px; top: 229px; width: 3px; height: 48px; background: var(--navy); }

  .contacts { position: absolute; left: 279px; top: 229px; list-style: none; }
  .contacts li { display: flex; align-items: center; height: 15.5px; font-size: 14.5px; letter-spacing: 0.02em; }
  .contacts svg { width: 9px; height: 9px; margin-right: 12px; fill: var(--navy); flex: none; }
</style>
</head>
<body>
  <section class="card card--contact">
    <div class="wordmark">
      <span class="wordmark__name">brennock</span>
      <span class="wordmark__tagline">Metal Recycling</span>
    </div>

    <div class="person">
      <p class="person__name">Gordon Brennock</p>
      <p class="person__role">Owner-Director</p>
    </div>
    <div class="divider"></div>

    <ul class="contacts">
      <li>
        <svg viewBox="0 0 10 10" aria-hidden="true"><path d="M2 0.5l1.6 2-0.9 1.1c0.6 1.2 1.4 2 2.6 2.6l1.1-0.9 2 1.6-1 2C4 9 1 6 0.5 1.5z"/></svg>
        000 0000 0000
      </li>
      <li>
        <svg viewBox="0 0 10 10" aria-hidden="true"><path d="M0 2h10v6H0z M0.5 2.3L5 5.6 9.5 2.3" stroke="#fbfafa" stroke-width="0.8"/></svg>
        info@brennockscrapworks.example.co.uk
      </li>
      <li>
        <svg viewBox="0 0 10 10" aria-hidden="true"><circle cx="5" cy="5" r="4.3" fill="none" stroke="#031f4e" stroke-width="1.2"/><path d="M3 3l2 1 1 2-1 2-1-2z"/></svg>
        brennockscrapworks.example.co.uk
      </li>
    </ul>
  </section>

  <section class="card card--brand">
    <div class="wordmark">
      <span class="wordmark__name">brennock</span>
      <span class="wordmark__tagline">Metal Recycling</span>
    </div>
  </section>
</body>
</html>
```